Book cover for a book about time management for women

We need a book cover for a book about time management for women written by a woman. Even though the book has a provocative title "Calendar candy" based on the seminars the author holds for women seeking the change in their life, it has nothing to do with the words themselves. The subtitle is "Keep each morning in your grip. A bold guide on daily rhythm for ladies today"

Preferred fonts (not necessarily):
Plus Jakarta Sans
Tiempos Headline

Preferred colours (not necessarily):
- orange
- pastel "highlighters"

We look for a simple/clean design that catches the attention of the women without too many graphic elements.

Target Market(s)

Women that want to change and organise their life

Industry/Entity Type

productivity, marketing, work-life balance

Font styles to use
Other font styles liked:
• Plus Jakarta Sans, Tiempos Headline

Colors
F0912C
F2A743
F7CA91
FBE8D2
FDF5EE
A7469A
B969AE
D3A5CF
EDDBEB
F8F0F9

Requirements
Must have
• Famine feeling as the target audience are women with drive to better life
Should not have
• No explicit images or sexually motivated themes

```html
<!DOCTYPE html>
<html lang="en">
<head>
<meta charset="utf-8">
<title>Calendar Candy — Book Cover</title>
<link href="https://fonts.googleapis.com/css2?family=Libre+Baskerville:wght@400;700&family=Source+Serif+4:opsz,wght@8..60,400;8..60,600&display=swap" rel="stylesheet">
<style>
  :root {
    --page: #ffffff;
    --sky-top: #6fbfcb;
    --sky-bottom: #a8dbe5;
    --floor: #f4dde4;
    --floor-deep: #ecd0d9;
    --navy: #34496b;
    --ink: #2f3438;
    --clock-light: #f8dbe6;
    --clock: #f1b4cb;
  }
  * { margin: 0; padding: 0; box-sizing: border-box; }
  html, body {
    width: 1200px; height: 1200px; overflow: hidden;
    background: var(--page);
  }
  .cover {
    position: absolute; left: 200px; top: 0;
    width: 800px; height: 1200px; overflow: hidden;
    background: linear-gradient(200deg, var(--sky-top) 0%, var(--sky-bottom) 75%);
    box-shadow: 0 0 14px rgba(0,0,0,0.25);
  }
  .floor {
    position: absolute; left: 0; top: 862px; width: 100%; height: 338px;
    background: linear-gradient(180deg, var(--floor) 0%, var(--floor-deep) 100%);
  }
  .kicker {
    position: absolute; top: 64px; left: 0; width: 100%;
    text-align: center;
    font-family: "Libre Baskerville", serif;
    font-size: 24px; line-height: 36px; letter-spacing: 4px;
    color: var(--navy);
  }
  .title-top {
    position: absolute; top: 268px; left: 40px; width: 720px;
    text-align: center;
    font-family: "Source Serif 4", serif; font-weight: 600;
    font-size: 78px; letter-spacing: -1px; color: var(--ink);
  }
  .title-main {
    position: absolute; top: 362px; left: 40px; width: 720px;
    text-align: center; white-space: nowrap;
    font-family: "Libre Baskerville", serif; font-weight: 400;
    font-size: 168px; line-height: 210px; letter-spacing: -4px;
    color: var(--navy);
  }
  .clock-scene {
    position: absolute; left: 250px; top: 600px; width: 200px; height: 440px;
    border-radius: 16px;
    background: linear-gradient(180deg, var(--clock-light) 0%, var(--clock) 100%);
  }
  .tagline {
    position: absolute; top: 608px; left: 466px;
    font-family: "Libre Baskerville", serif; white-space: nowrap;
    font-size: 32px; line-height: 52px; letter-spacing: -1px;
    color: var(--navy);
  }
  .tagline span { display: block; padding-left: 18px; }
  .author {
    position: absolute; top: 1100px; left: 0; width: 100%;
    text-align: center;
    font-family: "Libre Baskerville", serif;
    font-size: 44px; letter-spacing: 8px; color: var(--navy);
  }
</style>
</head>
<body>
  <main class="cover">
    <div class="floor"></div>
    <p class="kicker">A BOLD GUIDE ON<br>DAILY RHYTHM FOR LADIES TODAY</p>
    <h1>
      <span class="title-top">CALENDAR</span>
      <span class="title-main">CANDY</span>
    </h1>
    <div class="clock-scene" role="img" aria-label="Photo of pink alarm clocks falling into a hole in a pink floor"></div>
    <p class="tagline">Keep each morning<span>in your grip</span></p>
    <p class="author">AUTHOR NAME</p>
  </main>
</body>
</html>
```